Brochure

I already have Logo Design.

Target Market(s)

Corporate Customer, Banks, Financial Institute, General Public

Font styles to use
Serif

Requirements
Must have
• Nice Modern Cars, Some Graphics,
Nice to have
• Time Line where required
Should not have
• Glamour Pictures of Ladies

```html
<!DOCTYPE html>
<html lang="en">
<head>
<meta charset="utf-8">
<title>Velmora Brochure – Mission and Values Spread</title>
<link rel="stylesheet" href="https://fonts.googleapis.com/css2?family=Marcellus&display=swap">
<style>
  :root {
    --backdrop: #e6e6e6;
    --gold: #d6a21c;
    --gold-deep: #c28d12;
    --gold-light: #e2b53a;
    --brown: #7a5410;
    --cream: #fbf1d2;
    --ink-white: #ffffff;
    --photo-dark: #0d0d0e;
    --photo-mid: #3a3b3e;
    --photo-light: #9a9ca0;
  }
  * { box-sizing: border-box; margin: 0; padding: 0; }
  html, body {
    width: 1200px;
    height: 857px;
    overflow: hidden;
    background: var(--backdrop);
    font-family: "Marcellus", Georgia, serif;
  }
  .spread {
    position: absolute;
    left: 80px;
    top: 128px;
    width: 1040px;
    height: 600px;
    display: flex;
    box-shadow: 0 18px 40px rgba(0,0,0,0.18);
  }
  .page {
    position: relative;
    width: 520px;
    height: 600px;
    overflow: hidden;
  }
  .page--mission { background: var(--photo-dark); }
  .car-photo {
    position: absolute;
    inset: 0;
    width: 100%;
    height: 100%;
  }
  .mission-band {
    position: absolute;
    left: 0;
    top: 300px;
    width: 520px;
    height: 150px;
    background: rgba(214, 162, 28, 0.82);
    display: flex;
    align-items: center;
    padding: 0 26px;
    gap: 22px;
  }
  .mission-band__title {
    color: var(--cream);
    font-size: 30px;
    letter-spacing: 3px;
    align-self: flex-end;
    padding-bottom: 22px;
  }
  .mission-band__text {
    color: var(--ink-white);
    font-size: 11.5px;
    line-height: 1.55;
    max-width: 360px;
  }
  .mission-band__text strong { font-weight: normal; letter-spacing: 0.5px; }
  .page--values {
    background: linear-gradient(160deg, var(--gold-light) 0%, var(--gold) 45%, var(--gold-deep) 100%);
    padding: 64px 40px 0 48px;
  }
  .brand {
    display: flex;
    align-items: center;
    gap: 10px;
    margin-bottom: 26px;
  }
  .brand__mark {
    width: 30px;
    height: 30px;
    border-radius: 50%;
    background: var(--brown);
  }
  .brand__name {
    color: var(--brown);
    font-size: 26px;
  }
  .values__heading {
    color: var(--brown);
    font-size: 27px;
    font-weight: normal;
    letter-spacing: 2px;
    line-height: 1.25;
    margin-bottom: 30px;
  }
  .values__list {
    color: var(--cream);
    font-size: 25px;
    line-height: 1.55;
    letter-spacing: 0.5px;
  }
</style>
</head>
<body>
  <main class="spread">
    <section class="page page--mission">
      <svg class="car-photo" role="img" aria-label="Photograph of a glossy black modern luxury car, front three-quarter view with headlights and alloy wheel" viewBox="0 0 520 600" preserveAspectRatio="none">
        <defs>
          <radialGradient id="carSheen" cx="60%" cy="35%" r="70%">
            <stop offset="0%" stop-color="var(--photo-light)"/>
            <stop offset="35%" stop-color="var(--photo-mid)"/>
            <stop offset="100%" stop-color="var(--photo-dark)"/>
          </radialGradient>
        </defs>
        <rect width="520" height="600" fill="url(#carSheen)"/>
      </svg>
      <div class="mission-band">
        <h2 class="mission-band__title">MISSION</h2>
        <p class="mission-band__text">To be the most sought after car rental services provider in the market serving a broad spectrum of discerning customers – individuals, organizations and large corporations on the strength of our 3S Factors, <strong>SERVICE, SUPERIORITY</strong> and <strong>SYNERGY</strong>, to be recognized as the pioneering leader in innovation, Style, Luxury, Class, elegance and an inspiring experience to our customers, drive &amp; mile after mile.</p>
      </div>
    </section>
    <section class="page page--values">
      <div class="brand">
        <span class="brand__mark"></span>
        <span class="brand__name">Velmora</span>
      </div>
      <h2 class="values__heading">VALUES THAT DRIVE<br>OUR BUSINESS FORWARD</h2>
      <p class="values__list">Commitment. Drive. Initiative.<br>Innovation. Integrity. Quality.<br>Service. Consistency. Enhancement.<br>Passion. Teamwork. Transparency.<br>Cultural. Diversity. Due Diligence.</p>
    </section>
  </main>
</body>
</html>
```